Kalvoria - a property developer - Website design

Hi all!
Exciting new project for you! :)
We are looking for some creative/modern designs to best represent us as a company.
Please have a look at the following link: huhu.kalvoria.example to get an idea about who we are and what we do.
The 'Main Page' of the HP should be neatly arranged, easy to navigate, contain several pictures (changing every 10 seconds or so) that should reflect that we are property developers.
The navigation points ('About us', 'Projects' 'Investment', 'Contact Us', 'Legal Notice') should be included in the Design (again under every navigation point, pictures may be added - that reflect our profession and/or the subsection)
What we will need at the end of the day is a fully functional site - i.e: a site that is designed and programmed with backend/wordpress, to allow us to make changes anytime we feel like it.
Further questions?! Don't hesitate to contact me! Thanks :)
Target Market(s)
Real Estate Development/Building sector
Industry/Entity Type
Real Estate Development
Number of Pages Required
5+ page
Look and feel

```html
<!DOCTYPE html>
<html lang="en">
<head>
<meta charset="utf-8">
<title>Kalvoria – Property Developer</title>
<link href="https://fonts.googleapis.com/css2?family=Roboto+Condensed:wght@300;400;700&family=Arimo:wght@400;700&display=swap" rel="stylesheet">
<style>
:root{
  --teal:#4fc3c8;
  --teal-dark:#358283;
  --ink:#2b2b2b;
  --body:#3a3a3a;
  --page:#ffffff;
  --outer:#e6e6e6;
  --white:#ffffff;
}
*{margin:0;padding:0;box-sizing:border-box}
html,body{width:780px;height:1200px;overflow:hidden;background:var(--outer)}
body{font-family:"Roboto Condensed",sans-serif;color:var(--ink);position:relative}
.page{position:absolute;left:29px;top:0;width:720px;height:1200px;background:var(--page)}
.abs{position:absolute}

/* header */
.brand{left:15px;top:20px;display:flex;align-items:center;gap:6px}
.brand-mark{width:12px;height:26px;background:var(--ink)}
.brand-name{font-family:"Roboto Condensed",sans-serif;font-weight:300;font-size:27px;letter-spacing:1px;color:var(--ink);line-height:1}
.brand-sub{left:34px;top:45px;font-size:5px;color:var(--ink);letter-spacing:.3px}
.nav{right:21px;top:35px;display:flex;gap:20px;font-size:8px;font-weight:700;letter-spacing:.2px}
.nav a{color:var(--ink);text-decoration:none;padding-bottom:4px}
.nav a.active{border-bottom:1.5px solid var(--ink)}

/* hero */
.hero{left:0;top:75px;width:720px;height:275px;background:linear-gradient(120deg,#b09c80 0%,#e8e2d8 35%,#f4f1ec 55%,#d9c8ae 75%,#a8743f 100%)}
.hero-caption{left:452px;top:166px;width:261px;height:65px;background:var(--teal);padding:13px 18px;color:var(--white);font-size:11.5px;font-weight:400;line-height:16px}
.hero-dots{left:471px;top:227px;display:flex;gap:3px}
.hero-dots span{width:36px;height:2px;background:var(--white)}

/* intro */
.section-title{font-size:14.5px;font-weight:400;color:var(--ink);border-left:2px solid var(--teal);padding-left:7px;line-height:15px;letter-spacing:.1px}
.intro-title{left:15px;top:377px}
.intro-text{left:15px;top:411px;width:464px;font-size:7.6px;line-height:12px;color:var(--body);font-weight:400}
.intro-text p+p{margin-top:12px}
.intro-photo{left:504px;top:377px;width:206px;height:120px;background:linear-gradient(100deg,#d8d2c6 0%,#9fb07e 40%,#e6ddd0 70%,#b8834c 100%)}

/* projects */
.projects-title{left:15px;top:551px}
.project{top:594px;width:183px}
.project-photo{width:100%;height:89px}
.project-label{font-size:7.5px;font-weight:700;margin-top:11px;color:var(--ink)}
.project.active .project-label{margin-top:3px;background:var(--teal);color:var(--white);padding:4px 6px;height:21px}
.p1{left:15px}.p1 .project-photo{background:linear-gradient(180deg,#5f85b8 0%,#d5d9de 45%,#e2d3a0 75%,#7a7a6a 100%)}
.p2{left:255px;width:180px}.p2 .project-photo{background:linear-gradient(180deg,#d8dad8 0%,#b0aca4 60%,#8a6040 100%)}
.p3{left:491px}.p3 .project-photo{background:linear-gradient(160deg,#7d4a2e 0%,#e9e6e0 45%,#c9c0ad 100%)}

/* investment */
.invest{left:0;top:764px;width:720px;height:144px;background:var(--teal);color:var(--white)}
.invest-title{left:23px;top:16px;font-size:14.5px;font-weight:700;letter-spacing:.1px}
.invest-text{left:23px;top:50px;width:440px;font-size:7.8px;line-height:12px}
.invest-btn{left:23px;top:98px;width:206px;height:31px;background:var(--white);color:var(--ink);font-size:11px;font-weight:400;display:flex;align-items:center;justify-content:center;letter-spacing:.2px}
.invest-art{left:591px;top:12px;width:129px;height:132px;background:linear-gradient(160deg,#e0b050 0%,#4fc3c8 40%,#f0d6b0 70%,#b0481e 100%);opacity:.9}

/* partners & newsletter */
.small-head{font-size:7.5px;font-weight:700;color:var(--ink);letter-spacing:.2px}
.partners-head{left:25px;top:934px}
.partner{top:975px;display:flex;align-items:center;gap:6px;font-size:13px;font-weight:400;color:var(--ink)}
.partner i{display:block;width:14px;height:14px;background:var(--ink)}
.pa{left:25px}.pb{left:206px}.pc{left:370px}
.news-head{left:481px;top:934px}
.news-sub{left:481px;top:953px;font-size:8px;color:var(--body)}
.news-input{left:481px;top:974px;width:115px;height:20px;border:1px solid #cfcfcf;background:var(--white)}
.news-go{left:603px;top:974px;width:34px;height:20px;background:var(--teal);color:var(--white);font-size:7.5px;font-weight:700;display:flex;align-items:center;justify-content:center}

/* footer */
.footer{left:0;top:1078px;width:720px;height:122px;background:var(--teal-dark);color:var(--white);font-family:"Arimo",sans-serif}
.footer-contact{left:29px;top:18px;font-size:7.2px;font-weight:700;line-height:11px}
.footer-contact .gap{height:11px}
.footer-social{right:26px;top:23px;text-align:right}
.social-title{font-size:8.5px;font-weight:700}
.social-sub{font-size:6.8px;color:#9fc9c9;margin-top:1px}
.social-icons{display:flex;justify-content:flex-end;gap:5px;margin-top:3px}
.social-icons span{width:14px;height:14px;border-radius:2px}
.social-icons .s1{background:#ffffff}.social-icons .s2{background:#4bb0e6}.social-icons .s3{background:#c8302a}.social-icons .s4{background:#3b5a9a}
.footer-legal{right:26px;top:80px;text-align:right;font-size:6.8px;color:#a9d1d1;line-height:9px}
</style>
</head>
<body>
<div class="page">

  <header>
    <div class="abs brand"><span class="brand-mark"></span><span class="brand-name">KALVORIA</span></div>
    <div class="abs brand-sub">huhu.kalvoria.example</div>
    <nav class="abs nav">
      <a class="active">HOME</a><a>ABOUT US</a><a>PROJECTS</a><a>INVESTMENT</a><a>LEGAL NOTICE</a><a>CONTACT US</a>
    </nav>
  </header>

  <section>
    <div class="abs hero" role="img" aria-label="Sunlit attic apartment with wooden floor and roof windows"></div>
    <div class="abs hero-caption">SOLVAGASSE - APPARTMENTS<br>FULL CONSTRUCTION WORK</div>
    <div class="abs hero-dots"><span></span><span></span><span></span><span></span><span></span><span></span></div>
  </section>

  <section>
    <h2 class="abs section-title intro-title">QUALITY, SKILLS AND EXPERIENCE: EVERYTHING UNDER ONE ROOF.</h2>
    <div class="abs intro-text">
      <p>Kalvoria is a combination of potent companies pursuing a common goal: the realization of modern, sustainable housing projects for highest emands in Vienna. Our building companies' efforts are concentrating on the two core areas of new developments and roof extensions.</p>
      <p>A high level of expertise, excellent quality and many years of experience provide a solid foundation for the realization of dream homes. Our Kalvoria companies combine the knowledge and know-how of more than 30 years under one roof. We want our customers to be satisfied for a long time – whether they want to invest in property or use an apartment themselves. Consulting on an equal basis is the main objective in our customer relations, from the first meeting, to the handover date.</p>
    </div>
    <div class="abs intro-photo" role="img" aria-label="Bright living room with sofa and large windows to a green garden"></div>
  </section>

  <section>
    <h2 class="abs section-title projects-title">OUR PROJECTS</h2>
    <div class="abs project p1 active">
      <div class="project-photo" role="img" aria-label="Modern townhouse under a blue sky"></div>
      <div class="project-label">MIRABELWEG - TOWNHOUSE</div>
    </div>
    <div class="abs project p2">
      <div class="project-photo" role="img" aria-label="Open living space of a family house with wooden railing"></div>
      <div class="project-label">TANNERGASSE - FAMILY HOUSE</div>
    </div>
    <div class="abs project p3">
      <div class="project-photo" role="img" aria-label="Staircase with glass balustrade in a new apartment"></div>
      <div class="project-label">SOLVAGASSE - APPARTMENTS</div>
    </div>
  </section>

  <section class="abs invest">
    <h2 class="abs invest-title">BUILD UP ON A SAFE INVESTMENT.</h2>
    <p class="abs invest-text">Invest now in the future of housing. Starting with an investment from 300.000 Euro you can participate in an exclusive roof extension or new development project by Kalvoria. Benefit from uniquely successful projects with high returns and an entry in the land register.</p>
    <div class="abs invest-btn">GET IN TOUCH WITH US TODAY!</div>
    <div class="abs invest-art" role="img" aria-label="Illustration of a hand holding coins with a growing money plant"></div>
  </section>

  <section>
    <div class="abs small-head partners-head">KALVORIA IS A JOINT VENTURE BETWEEN:</div>
    <div class="abs partner pa"><i></i>Corvel Property</div>
    <div class="abs partner pb"><i></i>Maridon Real Estate</div>
    <div class="abs partner pc">Halden</div>

    <div class="abs small-head news-head">GET TO KNOW US MORE</div>
    <div class="abs news-sub">Subscribe to our weekly newsletter</div>
    <div class="abs news-input"></div>
    <div class="abs news-go">GO</div>
  </section>

  <footer class="abs footer">
    <div class="abs footer-contact">
      KALVORIA.EXAMPLE &amp; KALVORIA-GROUP.EXAMPLE
      <div class="gap"></div>
      MERLGASSE 12/TOP 5,&nbsp; 1220 VIENNA - AUSTRIA<br>
      PHONE: +43 1 555 0190<br>
      FAX: +43 1 555 0191<br>
      E-MAIL: INFO@KALVORIA.EXAMPLE
    </div>
    <div class="abs footer-social">
      <div class="social-title">Stay Connected</div>
      <div class="social-sub">Follow us for the latest updates and deals</div>
      <div class="social-icons"><span class="s1"></span><span class="s2"></span><span class="s3"></span><span class="s4"></span></div>
    </div>
    <div class="abs footer-legal">
      COPYRIGHT 2015. ALL RIGHTS RESERVED.<br>
      TERMS &amp; CONDITIONS&nbsp; - &nbsp;PRIVACY&nbsp; - &nbsp;DISCLAIMER
    </div>
  </footer>

</div>
</body>
</html>
```